Brisk Tide needs a web page for E-commerce site

Small startup business looking for a custom website for my New Saltwater apparel Co.

COMPANY OVERVIEW

Brisk Tide was founded In Mont Belvieu, Tx, right on the heart of pelican cove.

Brisk Tide is the adrenaline, sweat pumping moment you find yourself setting the hook on a monster fish. This is the moment when all your senses come to life as you work to land that trophy, and after a grueling fight when your hi-fiving your fishing buddies...It's that moment... when the waters and the air around you are Brisk Sweet....All or Nothing...pure Addiction......This is BRISK TIDE

Looking for a sharp clean sexy web page for my ecommerce page

I like the look of black background websites.

www.brisktidegear.example
Updates

I am using bigcommerce as my host site if that means anything to y'all

Thank you all for the submissions! There were some great ones!  I will have more projects in the future. thanks again

Target Market(s)

inshore/offshore fishing, saltwater enthusiast

Industry/Entity Type

Business

Requirements
Must have
• logo's

inshore/offshore fishing appeal

compatible with bigcommerce site

```html
<!DOCTYPE html>
<html lang="en">
<head>
<meta charset="utf-8">
<title>Brisk Tide – Sign In</title>
<link href="https://fonts.googleapis.com/css2?family=Play:wght@400;700&family=Roboto:wght@300;400&display=swap" rel="stylesheet">
<style>
:root{
  --black:#050505;
  --panel:#131416;
  --band:rgba(22,26,34,.82);
  --footer:rgba(24,28,36,.9);
  --link-grey:#a7a9ad;
  --text-grey:#5c5c5c;
  --heading-grey:#6a6a6a;
  --red:#a3151b;
  --white:#ffffff;
  --modal:#ffffff;
  --rule:#8a8a8a;
}
*{box-sizing:border-box;margin:0;padding:0}
html,body{width:1200px;height:891px;overflow:hidden;background:var(--black)}
body{position:relative;font-family:"Roboto",Arial,sans-serif;letter-spacing:.04em}
a{color:inherit;text-decoration:none}

.hero-photo{position:absolute;left:0;top:47px;width:1200px;height:844px;
  background:linear-gradient(100deg,#8fb6d4 0%,#5aa7c7 22%,#7ccfd8 34%,#bfe3e4 46%,#d9cdb3 58%,#c9a774 72%,#b78a55 86%,#c9b08a 100%);}
.hero-photo::after{content:"";position:absolute;inset:0;
  background:linear-gradient(180deg,rgba(150,180,205,.7) 0,rgba(160,190,210,.25) 35%,rgba(255,255,255,0) 55%,rgba(230,220,200,.25) 100%)}

.top-bar{position:absolute;left:0;top:0;width:1200px;height:47px;background:var(--black);border-bottom:1px solid #4a4d52;z-index:3}
.utility-links{position:absolute;left:121px;top:14px;font-size:12px;color:var(--link-grey);font-weight:300;white-space:nowrap}
.search{position:absolute;left:866px;top:11px;display:flex;align-items:center}
.search label{font-family:"Play",sans-serif;color:var(--white);font-size:14px;margin-right:11px}
.search .field{width:140px;height:25px;background:var(--white);font-size:12px;color:#222;padding:5px 8px;font-weight:400}
.search .go{width:28px;height:25px;background:var(--red);display:flex;align-items:center;justify-content:center}

.nav-band{position:absolute;left:0;top:47px;width:1200px;height:165px;background:var(--band);z-index:2}
.main-nav a{position:absolute;top:72px;font-family:"Play",sans-serif;font-size:25px;color:var(--white);letter-spacing:0}
.brand-shield{position:absolute;left:431px;top:47px;z-index:3}
.brand-name{position:absolute;left:431px;top:110px;width:338px;text-align:center;z-index:4;
  font-family:"Play",sans-serif;font-weight:700;font-size:40px;color:var(--white);letter-spacing:.03em}

.account-modal{position:absolute;left:382px;top:275px;width:422px;height:408px;background:var(--modal);
  border-radius:10px;box-shadow:0 2px 6px rgba(0,0,0,.45);z-index:5;color:var(--text-grey);font-size:12px}
.close-btn{position:absolute;left:774px;top:262px;z-index:6}
.modal-title{position:absolute;left:31px;font-family:"Play",sans-serif;font-size:19px;color:var(--heading-grey);letter-spacing:.01em;font-weight:400}
.benefits{position:absolute;left:34px;top:50px;line-height:17px;list-style:none;font-weight:300}
.text-link{color:var(--red);text-decoration:underline}
.divider{position:absolute;left:15px;top:200px;width:392px;border-top:1px solid var(--rule)}
.field-label{position:absolute;left:36px;font-weight:300}
.text-input{position:absolute;left:153px;width:204px;height:25px;border:1px solid #c4c4c4;background:linear-gradient(#e6e6e6,#fafafa)}
.sign-in-btn{position:absolute;left:155px;top:332px;width:74px;height:28px;background:var(--red);color:var(--white);
  font-size:12px;text-decoration:underline;display:flex;align-items:center;justify-content:center}

.slider-tab{position:absolute;left:520px;top:696px;z-index:2}
.site-footer{position:absolute;left:0;top:728px;width:1200px;height:163px;background:var(--footer);text-align:center;color:var(--link-grey);font-size:12px;font-weight:300}
.footer-links{margin-top:24px}
.copyright{margin-top:9px}
.social{position:absolute;left:531px;top:77px}
</style>
</head>
<body>

<div class="hero-photo" role="img" aria-label="Photo of a turquoise shoreline with white salt flats and sandy cliffs under a cloudy sky"></div>

<header class="top-bar">
  <nav class="utility-links">Home | Shipping &amp; Returns | My Account | Order Status | Wish Lists | Gift Certificates | View Cart | Sign in or Sign up</nav>
  <form class="search">
    <label>Search</label>
    <div class="field">Find Products</div>
    <div class="go"><svg width="11" height="11" viewBox="0 0 11 11"><path d="M1 0 L11 5.5 L1 11Z" fill="#fff"/></svg></div>
  </form>
</header>

<div class="nav-band">
  <nav class="main-nav">
    <a style="left:176px">Ladies</a>
    <a style="left:320px">Men</a>
    <a style="left:825px">Accessories</a>
    <a style="left:1022px">Sale</a>
  </nav>
</div>

<svg class="brand-shield" width="338" height="222" viewBox="0 0 338 222">
  <path d="M0 0 H338 V165 L169 220 L0 165Z" fill="#3a3d42"/>
  <path d="M0 0 H338 V163 L169 216 L0 163Z" fill="var(--panel)"/>
</svg>
<div class="brand-name">BRISK TIDE</div>

<section class="account-modal">
  <h2 class="modal-title" style="top:20px">Create a New Account</h2>
  <ul class="benefits">
    <li>Create an account with us and you'll be able to:</li>
    <li>&nbsp;</li>
    <li>- Check out faster</li>
    <li>- Save multiple shipping addresses</li>
    <li>- Access your order history</li>
    <li>- Track new orders</li>
    <li>- Save items to your wish list</li>
    <li><a class="text-link">Click here to create a new account.</a></li>
  </ul>
  <div class="divider"></div>
  <h2 class="modal-title" style="top:211px">Sign in to Your Account</h2>
  <p class="field-label" style="left:34px;top:240px">You need to sign in to access this page.</p>
  <span class="field-label" style="top:274px">Email Address</span>
  <div class="text-input" style="top:269px"></div>
  <span class="field-label" style="top:305px">Password</span>
  <div class="text-input" style="top:300px"></div>
  <a class="sign-in-btn">Sign In</a>
  <a class="text-link" style="position:absolute;left:159px;top:369px">Forgot your password?</a>
</section>

<svg class="close-btn" width="42" height="42" viewBox="0 0 42 42">
  <circle cx="21" cy="21" r="20" fill="#e9e9e9"/>
  <circle cx="21" cy="20" r="17" fill="#c0272d"/>
  <path d="M14 13 L28 27 M28 13 L14 27" stroke="#fff" stroke-width="3.2" stroke-linecap="round"/>
</svg>

<svg class="slider-tab" width="160" height="32" viewBox="0 0 160 32">
  <path d="M10 0 H150 L160 32 H0Z" fill="#3a3d43"/>
  <circle cx="48" cy="16" r="6.5" fill="#6a6c70"/>
  <circle cx="67" cy="16" r="6.5" fill="#141416"/>
  <circle cx="86" cy="16" r="6.5" fill="#6a6c70"/>
  <circle cx="104" cy="16" r="6.5" fill="#6a6c70"/>
</svg>

<footer class="site-footer">
  <p class="footer-links">My Account | Order Status | Wish Lists | Gift Certificates | View Cart | Sign in or Sign up</p>
  <p class="copyright">All prices are in USD. Copyright 2013 Brisk Tide Apperal Co.</p>
  <svg class="social" width="140" height="42" viewBox="0 0 140 42" aria-label="Social links">
    <circle cx="20" cy="20" r="20" fill="#3b5a98"/>
    <circle cx="67" cy="20" r="20" fill="#1d9bd1"/>
    <circle cx="114" cy="20" r="20" fill="#ee7a2e"/>
  </svg>
</footer>

</body>
</html>
```